Online Shop OKA

We need a web design for an online shop, called "OKA Bummel". The shop should layoutwise match with this head page: http://www.oka-gsund.at/, as it is a partner page. So please use similar, matching colors like the red, blue, white. The shop is supposed to be a platform for a certain commerce region in Austria. It should be available for rural local stores like bakeries, liquor stores, butchers, regional grocery stores or traditional costume stores to offer their products in the online shop. The look should be simple, traditional, clear and matching to the Oka-gsund page. If needed, you can google-search pictures of "Fuschlsee Salzburg" to use for background/banner etc. Others than that, pictures of food, traditional costumes (search word: austrian dirndl) are nice to be seen. Regarding Functions, the store will have the SAME functions as this page:http://www.velmora-markt.eu/ - using the "most famous" stores and its products for the starting page, going into detail pages by clicking these images. You can also think of a small area left for adverts of the local stores.

Target Market(s)

Target market are female as well as males, as well as families... Citizens of the countryside of this region in general as well as tourists of this region, looking online for individual local goods.

Industry/Entity Type

Shop

Requirements
Must have
• The design must have 3 pages: a starting page, a subsite with an overview for the different products of a certain store and a subsite with a product in detail.
• Please feel free to create some kind of a logo which is being used only online in the shop.
• Please think of the different "Stores" as categories, of different products of each store as the subpages and of a detailled description of one special product for the detail page.
Nice to have
• would be nice to have an emotional landscape image integrated in the design (such as you find for FUSCHLSEE SALZBURG in google) we dont have a proper picture yet.
Should not have
• the design should NOT look cheap or plain/technical. Emotions are of high importance as well as visual attraction for customers since we are selling good quality products of local stores and shops.

```html
<!DOCTYPE html>
<html lang="en">
<head>
<meta charset="utf-8">
<title>OKA Bummel – Online Shop</title>
<link rel="stylesheet" href="https://fonts.googleapis.com/css2?family=Open+Sans:wght@400;600;700&display=swap">
<style>
:root{
  --red:#c8102e;
  --red-dark:#8e0a0a;
  --red-btn:#d2332b;
  --blue:#3399cc;
  --blue-tab:#2e9bd0;
  --grey-bg:#c9c9c9;
  --text:#333;
  --muted:#555;
  --dark:#2b2b2b;
  --white:#fff;
}
*{box-sizing:border-box;margin:0;padding:0}
html,body{width:799px;height:1200px;overflow:hidden}
body{font-family:"Open Sans",sans-serif;color:var(--text);background:var(--grey-bg);position:relative}
.abs{position:absolute}
.header-band{left:0;top:0;width:799px;height:144px;background:linear-gradient(180deg,#b30a0a 0%,#9e0505 60%,#8a0303 100%)}
.brand{left:72px;top:28px;color:var(--white);font-weight:400}
.brand .small{font-size:16px;line-height:20px;display:block}
.brand .big{font-size:24px;line-height:30px;display:block}
.social{top:19px;display:flex;gap:6px;left:641px}
.social span{width:21px;height:21px;border-radius:3px;display:block}
.search{left:525px;top:51px;width:162px;height:21px;border-radius:11px;background:var(--white);box-shadow:inset 0 1px 3px rgba(0,0,0,.35)}
.search-btn{left:692px;top:51px;width:23px;height:23px}
.panel{left:70px;top:96px;width:659px;height:1054px;background:var(--white);border-radius:18px}
.nav{left:82px;top:111px;display:flex;font-size:11.5px;height:30px;align-items:center}
.nav a{color:#222;text-decoration:none;margin-right:25px}
.nav a.active{background:var(--blue-tab);color:var(--white);border-radius:6px 6px 0 0;height:30px;line-height:30px;padding:0 10px;margin-right:10px;margin-top:0}
.hero{left:82px;top:144px;width:635px;height:254px;background:linear-gradient(135deg,#6b8a4a 0%,#c46a9a 35%,#3a6a3a 55%,#7a5a8a 75%,#8a7a5a 100%)}
.hero-card{left:90px;top:178px;width:180px;height:188px;background:rgba(255,255,255,.88);padding:6px 10px}
.hero-card .kicker{font-size:13px;color:#333;letter-spacing:-.3px;margin-top:2px}
.hero-card h2{font-size:21px;color:var(--red);font-weight:600;letter-spacing:-.5px;line-height:22px}
.hero-card p{font-size:7.6px;line-height:10.2px;color:#333;margin-top:5px}
.price-tag{left:98px;top:298px;width:94px;height:33px;background:var(--red);color:var(--white);font-size:27px;line-height:33px;text-align:center;letter-spacing:-.5px}
.shop-now{left:98px;top:332px;width:93px;height:22px;background:var(--dark);color:var(--white);font-size:8.5px;line-height:22px;text-align:center}
.section-title{font-size:18px;color:var(--blue);font-weight:400}
.rule{left:82px;top:440px;width:635px;height:1px;background:#e6e6e6}
.product{width:158px}
.product .thumb{position:absolute;border-radius:4px}
.product .price{position:absolute;color:var(--blue);font-weight:700;font-size:12.5px}
.product .desc{position:absolute;font-size:6.8px;color:#444;white-space:nowrap}
.cart-btn{position:absolute;width:24px;height:24px;background:var(--dark);border-radius:2px}
.details-btn{position:absolute;width:60px;height:22px;background:var(--red-btn);color:var(--white);font-size:13px;line-height:22px;text-align:center}
.col-sep{width:1px;background:linear-gradient(180deg,rgba(0,0,0,0),rgba(0,0,0,.05),rgba(0,0,0,0))}
.row-sep{left:82px;top:645px;width:635px;height:1px;background:#eee}
.red-title{font-size:18px;color:var(--red);font-weight:400}
.cat-list{left:84px;top:872px;list-style:none;font-size:10px;color:#222}
.cat-list li{height:18.4px;line-height:18.4px}
.cat-list li::before{content:"›";font-weight:700;margin-right:6px}
.cart-box{left:83px;top:1052px;width:135px;height:72px;background:var(--dark);border:1px solid #555;color:var(--white);text-align:center}
.cart-box h3{font-size:11.5px;font-weight:600;line-height:28px;border-bottom:1px solid #555}
.cart-box p{font-size:12.5px;line-height:18px;margin-top:5px}
.cart-box .count{display:inline-block;background:#111;padding:0 4px;font-weight:700}
.liquor-img{left:243px;width:165px;height:118px}
.article{left:424px;width:291px}
.article h4{font-size:13.5px;font-weight:600;color:#333;line-height:18px}
.article .lead{font-size:8.8px;font-weight:700;color:#666;line-height:13px;margin-top:3px}
.article .body{font-size:8.5px;color:#555;line-height:13px;margin-top:5px}
.footer{top:1170px;font-size:7.5px;color:#333}
.footer-links{left:83px}
.footer-links a{color:#333;text-decoration:none}
.footer-copy{right:82px}
</style>
</head>
<body>
<div class="abs header-band"></div>
<div class="abs brand"><span class="small">Online Shop</span><span class="big">OKA Bummel</span></div>
<div class="abs social">
  <span style="background:#3b6db3"></span><span style="background:#f08a24"></span><span style="background:#39a9e0"></span>
</div>
<div class="abs search"></div>
<svg class="abs search-btn" viewBox="0 0 23 23" aria-hidden="true">
  <circle cx="11.5" cy="11.5" r="11" fill="#e8e8e8"/>
  <circle cx="11.5" cy="11.5" r="9" fill="#c02020"/>
  <circle cx="10.5" cy="10.5" r="3.6" fill="none" stroke="#fff" stroke-width="1.8"/>
  <line x1="13.2" y1="13.2" x2="16" y2="16" stroke="#fff" stroke-width="2" stroke-linecap="round"/>
</svg>

<div class="abs panel"></div>
<nav class="abs nav">
  <a class="active" href="#">Home</a><a href="#">Our Products</a><a href="#">About Us</a><a href="#">Special Offers</a><a href="#">Categories</a><a href="#">Contact Us</a>
</nav>

<div class="abs hero" role="img" aria-label="Women in traditional Austrian dirndl dresses walking through a festival crowd"></div>
<div class="abs hero-card">
  <div class="kicker">New Arrival Of</div>
  <h2>Austrian Dirndl</h2>
  <p>"Lorem ipsum dolor sit amet, consectetur adipisicing elit, sed do eiusmod tempor incididunt ut labore et dolore magna aliqua. Ut enim ad minim veniam, quis nostrud exercitation ullamco laboris nisi ut aliquip ex ea commodo consequat.</p>
</div>
<div class="abs price-tag">$25.89</div>
<div class="abs shop-now">Shop Now!</div>

<h2 class="abs section-title" style="left:82px;top:410px">Popular Products</h2>
<div class="abs rule"></div>
<div class="abs col-sep" style="left:239px;top:440px;height:400px"></div>
<div class="abs col-sep" style="left:405px;top:440px;height:400px"></div>
<div class="abs col-sep" style="left:572px;top:440px;height:400px"></div>
<div class="abs row-sep"></div>

<!-- row 1 -->
<div class="abs product" style="left:98px;top:0">
  <div class="thumb" style="left:0;top:452px;width:110px;height:90px;background:linear-gradient(90deg,#9aa88a,#c89ab0)" role="img" aria-label="Two dirndl dresses"></div>
  <div class="price" style="top:550px">$ 550.00</div><div class="desc" style="top:569px">Contrairement à une opinion répa.</div>
  <div class="cart-btn" style="top:585px"></div><div class="details-btn" style="left:33px;top:586px">Details</div>
</div>
<div class="abs product" style="left:265px;top:0">
  <div class="thumb" style="left:5px;top:450px;width:112px;height:92px;background:linear-gradient(135deg,#e8b24a,#3a70d0)" role="img" aria-label="Shopping basket full of groceries"></div>
  <div class="price" style="top:550px">$ 550.00</div><div class="desc" style="top:569px">Contrairement à une opinion répa.</div>
  <div class="cart-btn" style="top:585px"></div><div class="details-btn" style="left:33px;top:586px">Details</div>
</div>
<div class="abs product" style="left:422px;top:0">
  <div class="thumb" style="left:22px;top:452px;width:92px;height:90px;background:linear-gradient(90deg,#d8a0b8,#3a1a2a)" role="img" aria-label="Liqueur bottles with a cocktail glass"></div>
  <div class="price" style="top:550px">$ 550.00</div><div class="desc" style="top:569px">Contrairement à une opinion répa.</div>
  <div class="cart-btn" style="top:585px"></div><div class="details-btn" style="left:33px;top:586px">Details</div>
</div>
<div class="abs product" style="left:592px;top:0">
  <div class="thumb" style="left:14px;top:448px;width:60px;height:100px;background:linear-gradient(180deg,#3a2a2a,#c03030 60%,#eee)" role="img" aria-label="Woman wearing a red and black dirndl"></div>
  <div class="price" style="top:550px">$ 550.00</div><div class="desc" style="top:569px">Contrairement à une opinion répa.</div>
  <div class="cart-btn" style="top:585px"></div><div class="details-btn" style="left:33px;top:586px">Details</div>
</div>

<!-- row 2 -->
<div class="abs product" style="left:98px;top:0">
  <div class="thumb" style="left:2px;top:655px;width:108px;height:90px;background:linear-gradient(90deg,#c07820,#e8e8e0,#c8c8d8)" role="img" aria-label="Bottles of whisky, gin and vodka"></div>
  <div class="price" style="top:755px">$ 550.00</div><div class="desc" style="top:775px">Contrairement à une opinion répa.</div>
  <div class="cart-btn" style="top:790px"></div><div class="details-btn" style="left:33px;top:791px">Details</div>
</div>
<div class="abs product" style="left:265px;top:0">
  <div class="thumb" style="left:15px;top:658px;width:76px;height:86px;background:linear-gradient(180deg,#4a8a3a,#c8a070)" role="img" aria-label="Paper bag with fresh vegetables"></div>
  <div class="price" style="top:755px">$ 550.00</div><div class="desc" style="top:775px">Contrairement à une opinion répa.</div>
  <div class="cart-btn" style="top:790px"></div><div class="details-btn" style="left:33px;top:791px">Details</div>
</div>
<div class="abs product" style="left:422px;top:0">
  <div class="thumb" style="left:40px;top:652px;width:40px;height:96px;background:linear-gradient(180deg,#e060a0,#f070b8)" role="img" aria-label="Pink floral dress on a mannequin"></div>
  <div class="price" style="top:755px">$ 550.00</div><div class="desc" style="top:775px">Contrairement à une opinion répa.</div>
  <div class="cart-btn" style="top:790px"></div><div class="details-btn" style="left:33px;top:791px">Details</div>
</div>
<div class="abs product" style="left:592px;top:0">
  <div class="thumb" style="left:-6px;top:660px;width:130px;height:82px;background:linear-gradient(90deg,#d05030,#c8a070,#e8c040,#702070)" role="img" aria-label="Grocery bag surrounded by fruit and vegetables"></div>
  <div class="price" style="top:755px">$ 550.00</div><div class="desc" style="top:775px">Contrairement à une opinion répa.</div>
  <div class="cart-btn" style="top:790px"></div><div class="details-btn" style="left:33px;top:791px">Details</div>
</div>

<svg width="0" height="0" style="position:absolute" aria-hidden="true">
  <symbol id="cart" viewBox="0 0 24 24"><path d="M6 8h2l1.5 7h7l1.5-5H9" fill="none" stroke="#fff" stroke-width="1.8" stroke-linejoin="round"/><circle cx="10.5" cy="17.5" r="1.2" fill="#fff"/><circle cx="15.5" cy="17.5" r="1.2" fill="#fff"/></symbol>
</svg>
<svg class="abs" style="left:98px;top:585px" width="24" height="24"><use href="#cart"/></svg>
<svg class="abs" style="left:265px;top:585px" width="24" height="24"><use href="#cart"/></svg>
<svg class="abs" style="left:422px;top:585px" width="24" height="24"><use href="#cart"/></svg>
<svg class="abs" style="left:592px;top:585px" width="24" height="24"><use href="#cart"/></svg>
<svg class="abs" style="left:98px;top:790px" width="24" height="24"><use href="#cart"/></svg>
<svg class="abs" style="left:265px;top:790px" width="24" height="24"><use href="#cart"/></svg>
<svg class="abs" style="left:422px;top:790px" width="24" height="24"><use href="#cart"/></svg>
<svg class="abs" style="left:592px;top:790px" width="24" height="24"><use href="#cart"/></svg>

<h2 class="abs red-title" style="left:84px;top:837px">Categories</h2>
<ul class="abs cat-list">
  <li>Contrairementà</li><li>Uneopinion répandue</li><li>Psum n'est pas</li><li>Simplement du texte</li><li>Aléatoire Il trouve</li><li>Racines dans</li><li>Une oeuvre de</li><li>Littérature latine</li><li>Classique datant de</li>
</ul>
<div class="abs cart-box">
  <h3>SHOPPING CART</h3>
  <p>Now in your<br>cart <span class="count">0</span> items</p>
</div>

<h2 class="abs red-title" style="left:243px;top:837px">Top Ten Liquors</h2>
<div class="abs liquor-img" style="top:875px;background:linear-gradient(90deg,#5a3a1a,#c8a060,#4a5a3a,#8a2a1a)" role="img" aria-label="Shelf of assorted liquor bottles"></div>
<div class="abs liquor-img" style="top:1006px;background:linear-gradient(180deg,#1a1408,#4a3010 60%,#2a1a0a)" role="img" aria-label="Row of liquor bottles lit against a dark background"></div>

<div class="abs article" style="top:871px">
  <h4>Une recherche pour lorem Ipsu</h4>
  <p class="lead">Plusieurs variations de Lorem Ipsum peuvent être trouvées ici ou là, mais la majeure partie d'entre elles a été altérée par l'addition d'humour ou de mots aléatoires qui ne ressemblent pas une seconde à du texte standard.</p>
  <p class="body">Le Lorem Ipsum est simplement du faux texte employé dans la composition et la mise en page avant impression. Le Lorem Ipsum est le faux texte standard de l'imprimerie depuis les années 1500.</p>
</div>
<div class="abs article" style="top:1002px">
  <h4>Une recherche pour lorem Ipsu</h4>
  <p class="lead">Plusieurs variations de Lorem Ipsum peuvent être trouvées ici ou là, mais la majeure partie d'entre elles a été altérée par l'addition d'humour ou de mots aléatoires qui ne ressemblent pas une seconde à du texte standard.</p>
  <p class="body">Le Lorem Ipsum est simplement du faux texte employé dans la composition et la mise en page avant impression. Le Lorem Ipsum est le faux texte standard de l'imprimerie depuis les années 1500.</p>
</div>

<div class="abs footer footer-links"><a href="#">Home</a> &nbsp;| &nbsp;<a href="#">Our Products</a> &nbsp;| &nbsp;<a href="#">Special Offers</a> &nbsp;| &nbsp;<a href="#">About Us</a> &nbsp;| &nbsp;<a href="#">Categories</a> &nbsp;| &nbsp;<a href="#">Contact Us</a></div>
<div class="abs footer footer-copy">© Copyrights 2013 All rights Reserved</div>
</body>
</html>
```